Innovation and Optimisation Consultancy business needs a Wix website design

The task details are in the attached project brief. The attached pdf should give you a good outline of what is required. Colour guidance and look and feel guidelines are in the pdf file. The company is based in S.E.Asia.

Can be done as design files, but prefer it to be designed direct in WIX.

If you have any questions just ask.

I really don't know what will attract clients to my website so am leaving it to you to do something inspiring and innovative.

Target Market(s)

Organisations that don't just want to compete in their market, but that want to be number one in their market and be sure they stay there.

Industry/Entity Type

All

Requirements
Must have
• I don't know, I specialise in optimising businesses and inventing new products.
Nice to have
• Surprise me.

```html
<!DOCTYPE html>
<html lang="en">
<head>
<meta charset="utf-8">
<title>Novaris Works — Innovation &amp; Optimisation Consultancy</title>
<link href="https://fonts.googleapis.com/css2?family=Poppins:wght@300;400;500;600;700;800&display=swap" rel="stylesheet">
<style>
:root{
  --navy:#0c2461;
  --navy-deep:#0a1f55;
  --accent:#1c4fa3;
  --slate:#5d6b88;
  --ink:#1b1b1f;
  --text:#3a3d45;
  --muted:#6b7080;
  --soft-bg:#eef2f7;
  --white:#ffffff;
  --star:#f5a623;
}
*{box-sizing:border-box;margin:0;padding:0}
html,body{width:1200px;height:4246px;overflow:hidden}
body{position:relative;font-family:"Poppins",sans-serif;color:var(--text);background:var(--white)}
.abs{position:absolute}
.btn{position:absolute;display:flex;align-items:center;justify-content:center;border-radius:24px;color:var(--white);font-weight:600;font-size:14px;background:linear-gradient(90deg,#6a7896,var(--navy-deep));}
/* header */
.site-header{left:0;top:0;width:1200px;height:85px;background:var(--white)}
.brand{font-family:"Poppins",sans-serif;font-weight:800;font-size:23px;color:#2b2b2b;letter-spacing:.3px}
.nav a{position:absolute;top:28px;font-size:14px;color:#444;text-decoration:none}
.nav .active{color:var(--accent);font-weight:500}
.agent-label{font-size:12px;letter-spacing:3px;color:#666}
.agent-number{font-size:22px;font-weight:700;color:#111}
/* hero */
.hero{left:0;top:85px;width:1200px;height:553px;background:linear-gradient(100deg,#2c3a35 0%,#50655f 35%,#8b9aa0 65%,#c5ccd1 100%)}
.hero-welcome{left:115px;top:196px;color:#fff;font-size:16px}
.hero-title{left:113px;top:225px;color:#fff;font-size:52px;font-weight:700;line-height:1.1}
.hero-title span{font-weight:300}
.hero-btn{left:117px;top:304px;width:237px;height:44px;border:2px solid #fff;border-radius:24px;color:#fff;display:flex;align-items:center;justify-content:center;font-size:14px;font-weight:600;background:rgba(12,36,97,.55)}
.dot{position:absolute;width:13px;height:13px;border-radius:50%;border:1.5px solid rgba(255,255,255,.8)}
/* section titles */
.sec-title{font-size:34px;font-weight:600;color:var(--ink)}
.sec-title b{color:var(--navy);font-weight:600}
.rule{position:absolute;height:1.5px;background:var(--accent)}
.rule::before{content:"";position:absolute;left:-5px;top:-4.5px;width:10px;height:10px;border-radius:50%;background:var(--navy)}
.body-copy{font-size:15px;line-height:27.5px;color:var(--text)}
.photo{position:absolute;border-radius:6px}
.block{position:absolute;background:var(--navy);border-radius:6px}
/* solutions */
.solutions{left:0;top:1905px;width:1200px;height:582px;background:var(--soft-bg)}
.card{position:absolute;top:205px;width:218px;height:285px;border-radius:8px;background:linear-gradient(135deg,#6c7894 0%,#2b3c6b 60%,var(--navy-deep) 100%);color:#fff;text-align:center;box-shadow:0 6px 18px rgba(10,31,85,.2)}
.card.selected{border:4px solid #1a1a1a}
.card svg{margin-top:36px}
.card h3{font-size:18px;font-weight:600;margin-top:18px}
.card p{font-size:12px;line-height:17px;margin:8px 18px 0}
.card a{display:block;margin-top:14px;font-size:11px;font-weight:600;color:#fff;text-decoration:underline}
/* testimonials */
.quote-card{position:absolute;top:2697px;width:449px;height:225px;background:#fff;border-radius:10px;box-shadow:0 6px 20px rgba(0,0,0,.12);padding:38px 18px 0 13px}
.quote-card h4{font-size:16px;font-weight:500;font-style:italic;color:var(--navy)}
.quote-card p{font-size:12.3px;line-height:20.5px;text-align:center;margin-top:8px;color:#444}
.stars{position:absolute;right:18px;top:38px;color:var(--star);font-size:17px;letter-spacing:2px}
.tail{position:absolute;top:2915px;width:40px;height:40px;background:#fff;transform:skewX(-30deg);box-shadow:4px 6px 8px rgba(0,0,0,.06)}
.avatar{position:absolute;top:2957px;width:56px;height:56px;border-radius:50%;border:3px solid #fff;box-shadow:0 0 0 2px var(--navy);background:linear-gradient(160deg,#c9b8a8,#6d5a4d)}
.person-name{font-size:16px;color:var(--navy);font-weight:500}
.person-role{font-size:13px;color:#555}
/* contact */
.contact{left:0;top:3188px;width:1200px;height:692px;background:radial-gradient(ellipse at 80% 70%,#1d3d8a 0%,var(--navy) 55%,#0a1e52 100%)}
.field{position:absolute;left:275px;width:650px;height:42px;background:#fff;border-radius:2px;display:flex;align-items:flex-start;padding:12px 16px;font-size:13px;color:#333;gap:14px}
/* footer */
.footer{left:0;top:3880px;width:1200px;height:366px;background:#0b1330}
.foot-h{font-size:19px;font-weight:600;color:#fff}
.foot-u{position:absolute;width:46px;height:2px;background:#fff}
.foot-links{font-size:12px;line-height:26px;color:#d9dce6;list-style:none}
.social{position:absolute;top:4064px;width:25px;height:25px;border-radius:50%;border:1.5px solid #fff}
.ct-item{position:absolute;left:662px;display:flex;gap:12px;align-items:center;color:#fff}
.ct-icon{width:26px;height:26px;border-radius:50%;border:1.5px solid #3b68c4;display:flex;align-items:center;justify-content:center}
.ct-text small{display:block;font-size:8px;color:#aab}
.ct-text span{font-size:10px}
</style>
</head>
<body>

<!-- Header -->
<header class="abs site-header">
  <div class="abs brand" style="left:108px;top:24px">NOVARIS WORKS</div>
  <nav class="nav">
    <span class="abs" style="left:461px;top:18px;width:8px;height:2px;background:var(--accent)"></span>
    <a class="active" style="left:443px">Home</a>
    <a style="left:523px">About Us</a>
    <a style="left:624px">Services</a>
  </nav>
  <div class="btn" style="left:710px;top:15px;width:143px;height:45px;font-size:14px">Contact Us</div>
  <svg class="abs" style="left:879px;top:18px" width="42" height="42" viewBox="0 0 42 42"><circle cx="21" cy="21" r="19" fill="none" stroke="var(--navy)" stroke-width="2"/><path d="M14 13c1-1 2.5-1 3.2 0l2 3c.5.8.3 1.7-.3 2.3l-1 1c1 2.2 2.6 3.8 4.8 4.8l1-1c.6-.6 1.5-.8 2.3-.3l3 2c1 .7 1 2.2 0 3.2l-1.2 1.2c-1.2 1.2-3 1.4-4.5.6-4.5-2.4-8-5.9-10.4-10.4-.8-1.5-.6-3.3.6-4.5z" fill="var(--navy)"/></svg>
  <div class="abs agent-label" style="left:935px;top:15px">Talk to an agent</div>
  <div class="abs agent-number" style="left:934px;top:32px">555.014.2271</div>
</header>

<!-- Hero -->
<section class="abs hero" role="img" aria-label="Photo of a smiling businesswoman holding a tablet in a bright modern office">
  <div class="abs hero-welcome">Welcome to</div>
  <h1 class="abs hero-title">Novaris <span>Works</span></h1>
  <div class="abs hero-btn">Book An Appointment</div>
  <span class="dot" style="left:113px;top:515px"></span>
  <span class="dot" style="left:142px;top:515px"></span>
  <span class="dot" style="left:170px;top:515px;background:rgba(255,255,255,.6);box-shadow:0 0 0 3px rgba(255,255,255,.25)"></span>
  <span class="dot" style="left:198px;top:515px"></span>
</section>

<!-- About -->
<section class="about">
  <div class="block" style="left:107px;top:760px;width:162px;height:124px"></div>
  <div class="photo" role="img" aria-label="Photo of three colleagues smiling in a meeting room" style="left:122px;top:774px;width:391px;height:318px;background:linear-gradient(135deg,#d9dde0,#a8b0b5 50%,#6f7a80)"></div>
  <div class="photo" role="img" aria-label="Photo of two colleagues reviewing work on a laptop" style="left:402px;top:988px;width:184px;height:152px;border:4px solid #fff;box-shadow:0 4px 14px rgba(0,0,0,.25);background:linear-gradient(135deg,#e3e6ea,#8d98a3)"></div>
  <h2 class="abs sec-title" style="left:637px;top:734px">About <b>Us</b></h2>
  <span class="rule" style="left:643px;top:790px;width:55px"></span>
  <div class="abs" style="left:637px;top:818px;width:460px;font-size:19px;font-weight:600;line-height:30px;color:#333">Gaerspiciatis unde omse snis iste natus error sseit voluptatem accusanti.</div>
  <p class="abs body-copy" style="left:637px;top:887px;width:456px;text-align:justify">Gaerspiciatis unde omnis iste natus error sseit voluptatem accusantium doloremque laudan seftium, tsetam aseeem aperiam, eaque ipsa quae ab illo inventore veritatis et quasi architecto beatae vitae dicta sunt explicabo. Nemo enim ipsam voluptatem quia voluptas sit aspernatur aut odit aut fugit, sed quia consequuntur magni dolores eos qui ratione voluptatem sequi.</p>
  <div class="btn" style="left:637px;top:1096px;width:144px;height:46px">Learn More</div>
  <svg class="abs" style="left:590px;top:1172px" width="120" height="135" viewBox="0 0 120 135"><path d="M115 2v50c0 8-4 12-12 12H15c-8 0-12 4-12 12v57" fill="none" stroke="#555" stroke-width="1.2" stroke-dasharray="3 3"/></svg>
</section>

<!-- Benefits -->
<section class="benefits">
  <h2 class="abs sec-title" style="left:0;width:1200px;text-align:center;top:1302px">Benefits</h2>
  <span class="rule" style="left:553px;top:1360px;width:100px"></span>
  <p class="abs" style="left:290px;top:1374px;width:620px;text-align:center;font-size:17px;line-height:28px;color:#222">Gaerspiciatis unde omnis iste natus error sseit voluptatem accusantium doloremque laudan seftium</p>
  <p class="abs body-copy" style="left:118px;top:1468px;width:457px;text-align:justify;text-align-last:right">Karpiciatis unde omnis iste natus error sseit voluptatem accusantium doloremque laudan seftium, tsetam aseeem aperiam, eaque ipsa quae ab illo inventore veritatis et quasi architecto beatae vitae dicta sunt explicabo. Nemo enim ipsam voluptatem quia voluptas sit aspernatur aut odit aut fugit, sed quia consequuntur magni dolores eos qui ratione voluptatem sequi.</p>
  <div class="btn" style="left:433px;top:1696px;width:144px;height:46px">Learn More</div>
  <div class="block" style="left:925px;top:1427px;width:125px;height:120px"></div>
  <div class="photo" role="img" aria-label="Photo of two businessmen shaking hands across a desk" style="left:640px;top:1443px;width:392px;height:320px;background:linear-gradient(120deg,#4a3a2c,#8a6f55 40%,#b9c2cc 70%,#dfe4ea)"></div>
</section>

<!-- Our Solution -->
<section class="abs solutions">
  <h2 class="abs sec-title" style="left:0;width:1200px;text-align:center;top:84px">Our <b>Solution</b></h2>
  <span class="rule" style="left:535px;top:140px;width:100px"></span>

  <div class="card" style="left:115px">
    <svg width="60" height="60" viewBox="0 0 60 60" fill="none" stroke="#fff" stroke-width="1.8"><rect x="6" y="8" width="12" height="10" rx="2"/><rect x="40" y="8" width="14" height="10" rx="2"/><rect x="22" y="4" width="14" height="14" rx="2"/><path d="M10 30h40v22H10zM16 36h28M16 42h20"/></svg>
    <h3>Faerspicia Detisund</h3>
    <p>Karpiciatis unde omnis iste natus error sseit voluptatem accusantium doloremque laudan seftium.</p>
    <a>Learn More</a>
  </div>
  <div class="card" style="left:366px">
    <svg width="60" height="60" viewBox="0 0 60 60" fill="none" stroke="#fff" stroke-width="1.8"><path d="M34 22v-8M40 22V8M46 22v-11M52 22V4M30 24h26"/><circle cx="44" cy="42" r="7"/><circle cx="44" cy="42" r="2.5"/><path d="M6 56c0-10 6-16 14-16s14 6 14 16z"/></svg>
    <h3>Faerspicia Detisund</h3>
    <p>Karpiciatis unde omnis iste natus error sseit voluptatem accusantium doloremque laudan seftium.</p>
    <a>Learn More</a>
  </div>
  <div class="card selected" style="left:617px">
    <svg width="60" height="60" viewBox="0 0 60 60" fill="none" stroke="#fff" stroke-width="1.8"><rect x="4" y="6" width="34" height="26" rx="3"/><path d="M12 26v-8M19 26V14M26 26v-10M14 32l-4 10M28 32l4 10"/><circle cx="44" cy="38" r="10"/><circle cx="44" cy="38" r="3.5"/></svg>
    <h3>Faerspicia Detisund</h3>
    <p>Karpiciatis unde omnis iste natus error sseit voluptatem accusantium doloremque laudan seftium.</p>
    <a>Learn More</a>
  </div>
  <div class="card" style="left:869px">
    <svg width="60" height="60" viewBox="0 0 60 60" fill="none" stroke="#fff" stroke-width="1.8"><rect x="20" y="4" width="26" height="20" rx="3"/><path d="M26 11h14M26 17h10M30 24l-4 6M4 44l10-6h14c3 0 3 4 0 4H20M14 54l18-2 22-14c2-2 0-5-3-4L38 42"/></svg>
    <h3>Faerspicia Detisund</h3>
    <p>Karpiciatis unde omnis iste natus error sseit voluptatem accusantium doloremque laudan seftium.</p>
    <a>Learn More</a>
  </div>
</section>

<!-- Testimonials -->
<section class="testimonials">
  <h2 class="abs sec-title" style="left:0;width:1200px;text-align:center;top:2592px">Testimonials</h2>
  <span class="rule" style="left:553px;top:2650px;width:100px"></span>

  <div class="tail" style="left:205px"></div>
  <article class="quote-card" style="left:120px">
    <div class="stars">★★★★★</div>
    <h4>Amazing Experience!</h4>
    <p>"Karsp asesdiciatis unde omnis iste natus error sisaeset voluptatem accusantium doloremque laudantium, totam rem aperiam, eaque ipsases quae ab illo inventore veritatis eset quaseseseasi architecto bascaes aseseatae vitae dicta sunt explicabo. Nemo esesnim ipsam voluptatem quia voluptas sit aspernatur asaut odseit aut fugitsed quia consequuntur."</p>
  </article>
  <div class="avatar" role="img" aria-label="Portrait of the client" style="left:241px"></div>
  <div class="abs person-name" style="left:310px;top:2950px">Daniel Reyes</div>
  <div class="abs person-role" style="left:310px;top:2975px">Orvane Labs, CEO</div>

  <div class="tail" style="left:706px"></div>
  <article class="quote-card" style="left:621px">
    <div class="stars">★★★★★</div>
    <h4>Amazing Experience!</h4>
    <p>"Karsp asesdiciatis unde omnis iste natus error sisaeset voluptatem accusantium doloremque laudantium, totam rem aperiam, eaque ipsases quae ab illo inventore veritatis eset quaseseseasi architecto bascaes aseseatae vitae dicta sunt explicabo. Nemo esesnim ipsam voluptatem quia voluptas sit aspernatur asaut odseit aut fugitsed quia consequuntur."</p>
  </article>
  <div class="avatar" role="img" aria-label="Portrait of the client" style="left:743px;background:linear-gradient(160deg,#d8c2ae,#7a5b48)"></div>
  <div class="abs person-name" style="left:811px;top:2950px">Daniel Reyes</div>
  <div class="abs person-role" style="left:811px;top:2975px">Orvane Labs, CEO</div>

  <span class="dot" style="left:557px;top:3057px;border-color:var(--navy)"></span>
  <span class="dot" style="left:584px;top:3057px;border-color:var(--navy)"></span>
  <span class="dot" style="left:609px;top:3055px;width:18px;height:18px;border-color:var(--navy);box-shadow:inset 0 0 0 3px #fff;background:var(--navy)"></span>
  <span class="dot" style="left:641px;top:3057px;border-color:var(--navy)"></span>
</section>

<!-- Contact -->
<section class="abs contact">
  <h2 class="abs sec-title" style="left:0;width:1200px;text-align:center;top:108px;color:#fff">Contact Us</h2>
  <span class="rule" style="left:553px;top:165px;width:100px;background:#fff"></span>
  <div class="field" style="top:209px"><svg width="14" height="14" viewBox="0 0 14 14"><circle cx="7" cy="4" r="3" fill="#1f6fd1"/><path d="M1 14c0-4 3-6 6-6s6 2 6 6z" fill="#1f6fd1"/></svg>Your Name</div>
  <div class="field" style="top:269px"><svg width="16" height="12" viewBox="0 0 16 12"><rect x="0.5" y="0.5" width="15" height="11" fill="none" stroke="#1f6fd1"/><path d="M1 1l7 6 7-6" fill="none" stroke="#1f6fd1"/></svg>Email</div>
  <div class="field" style="top:329px"><svg width="14" height="14" viewBox="0 0 14 14"><path d="M2 1c.6-.6 1.5-.6 2 0l1.3 1.8c.3.5.2 1-.2 1.4l-.6.6c.6 1.4 1.6 2.4 3 3l.6-.6c.4-.4 1-.5 1.4-.2L11.3 8.3c.6.5.6 1.4 0 2l-.8.8c-.8.8-2 .9-3 .4C4.7 10 3 8.3 1.5 5.5 1 4.5 1.1 3.3 1.9 2.5z" fill="#1f6fd1"/></svg>Phone Number</div>
  <div class="field" style="top:389px;height:125px"><svg width="16" height="14" viewBox="0 0 16 14"><path d="M1 1h10v7H5l-3 3V8H1z" fill="#1f6fd1"/><path d="M12 4h3v7h-1v2l-2-2H7V9h5z" fill="#1f6fd1"/></svg>Write&nbsp; A Message</div>
  <div class="btn" style="left:527px;top:540px;width:145px;height:44px;background:#6c7590;border-radius:22px">Send Message</div>
</section>

<!-- Footer -->
<footer class="abs footer">
  <div class="abs brand" style="left:30px;top:125px;color:#fff;font-size:24px">NOVARIS WORKS</div>
  <span class="social" style="left:66px"></span>
  <span class="social" style="left:103px;background:#1f6fd1;border-color:#1f6fd1"></span>
  <span class="social" style="left:141px"></span>

  <div class="abs foot-h" style="left:257px;top:63px">Quick Links</div>
  <span class="foot-u" style="left:259px;top:98px"></span>
  <ul class="abs foot-links" style="left:259px;top:120px"><li>Home</li><li>About Us</li><li>Our Services</li><li>Contact Us</li></ul>

  <div class="abs foot-h" style="left:446px;top:63px">Customer info</div>
  <span class="foot-u" style="left:448px;top:98px"></span>
  <ul class="abs foot-links" style="left:448px;top:120px"><li>Team</li><li>About Us</li><li>Careers</li><li>Our Values</li></ul>

  <div class="abs foot-h" style="left:662px;top:63px">Contact Us</div>
  <span class="foot-u" style="left:664px;top:98px"></span>
  <div class="ct-item" style="top:127px"><span class="ct-icon"><svg width="12" height="12" viewBox="0 0 14 14"><path d="M2 1c.6-.6 1.5-.6 2 0l1.3 1.8c.3.5.2 1-.2 1.4l-.6.6c.6 1.4 1.6 2.4 3 3l.6-.6c.4-.4 1-.5 1.4-.2L11.3 8.3c.6.5.6 1.4 0 2l-.8.8c-.8.8-2 .9-3 .4C4.7 10 3 8.3 1.5 5.5 1 4.5 1.1 3.3 1.9 2.5z" fill="#3b7ae0"/></svg></span><div class="ct-text"><small>Call Us</small><span>+1 (555) 014 2271</span></div></div>
  <div class="ct-item" style="top:173px"><span class="ct-icon"><svg width="12" height="10" viewBox="0 0 16 12"><rect x="0.5" y="0.5" width="15" height="11" fill="#3b7ae0"/><path d="M1 1l7 6 7-6" fill="none" stroke="#0b1330"/></svg></span><div class="ct-text"><small>Email</small><span>hello@novarisworks.com</span></div></div>
  <div class="ct-item" style="top:219px"><span class="ct-icon"><svg width="10" height="13" viewBox="0 0 10 13"><path d="M5 0a5 5 0 0 1 5 5c0 3.5-5 8-5 8S0 8.5 0 5a5 5 0 0 1 5-5z" fill="#3b7ae0"/><circle cx="5" cy="5" r="1.8" fill="#0b1330"/></svg></span><div class="ct-text"><small>Address</small><span>218 Harbour Lane, Singapore 049315</span></div></div>

  <div class="abs foot-h" style="left:942px;top:63px">Newsletter signup</div>
  <span class="foot-u" style="left:944px;top:98px"></span>
  <p class="abs" style="left:942px;top:118px;width:215px;font-size:11.5px;line-height:19px;color:#d9dce6">Be the first to know about our new arrivals and exclusive offers!</p>
  <div class="abs" style="left:942px;top:165px;width:203px;height:30px;border-radius:15px;background:#fff;font-size:9px;color:#333;padding:9px 22px">EMAIL</div>
  <div class="btn" style="left:942px;top:209px;width:101px;height:31px;font-size:10px;background:linear-gradient(90deg,#5f6d8c,#1e3170)">Submit</div>

  <div class="abs" style="left:110px;top:300px;width:980px;height:1.5px;background:#2b55b8"></div>
  <div class="abs" style="left:0;width:1200px;top:328px;text-align:center;font-size:12px;color:#c9ccd6">© Copyright 2025. All rights reserved.</div>
</footer>

</body>
</html>
```